Crimson Vantage Cleaning Solutions

Need a logo and business card design. I want to use a translucent business card. I want to abbreviate the name C.V.C.S. Commercial Cleaning, because my is Dov. I’d also like to incorporate a knight or something like that. I want the idea to tie in with the word Crimson. New ideas are welcome, i don’t want to limit anyone’s creativity.

Target Market(s)

Commercial Cleaning for businesses.

Contact Information for Business Card

Crimson
Vantage
Cleaning
Solutions

```html
<!DOCTYPE html>
<html lang="en">
<head>
<meta charset="utf-8">
<title>Crimson Vantage Cleaning Solutions – Business Card</title>
<link rel="stylesheet" href="https://fonts.googleapis.com/css2?family=Arimo:wght@400;700&display=swap">
<style>
  :root {
    --page-bg: #e4e7ec;
    --card-top: #f6f7f9;
    --navy: #060b18;
    --gold: #d4a017;
    --gold-deep: #b8860b;
    --silver: #c7cad3;
    --text-light: #c9ccd6;
  }
  * { margin: 0; padding: 0; box-sizing: border-box; }
  html, body { width: 1200px; height: 970px; overflow: hidden; }
  body {
    background: var(--page-bg);
    font-family: "Arimo", Arial, sans-serif;
    position: relative;
  }
  .business-card {
    position: absolute;
    left: 100px; top: 200px;
    width: 1000px; height: 570px;
    border-radius: 28px;
    overflow: hidden;
    background: linear-gradient(180deg, #ffffff 0%, var(--card-top) 60%, #e8ebf0 100%);
    box-shadow: 0 18px 40px rgba(6, 11, 24, 0.22);
  }
  .card-waves { position: absolute; inset: 0; width: 100%; height: 100%; }
  .brand {
    position: absolute; left: 58px; top: 62px;
    display: flex; align-items: center; gap: 28px;
  }
  .brand-mark {
    width: 150px; height: 150px; border-radius: 50%;
    background: var(--gold);
    flex: none;
  }
  .brand-name {
    color: var(--navy);
    font-weight: 700;
    font-size: 58px;
    line-height: 1.08;
    width: 700px;
  }
  .person { position: absolute; left: 60px; top: 372px; }
  .person-name { color: var(--text-light); font-weight: 700; font-size: 34px; }
  .person-role { color: var(--gold); font-size: 24px; margin-top: 2px; }
  .contact-list { position: absolute; left: 60px; top: 455px; list-style: none; }
  .contact-list li {
    display: flex; align-items: center; gap: 14px;
    color: var(--text-light); font-size: 25px; height: 33px;
  }
  .contact-list svg { width: 24px; height: 24px; flex: none; }
  .address {
    position: absolute; left: 640px; top: 470px;
    color: var(--text-light); font-size: 25px; line-height: 33px;
  }
</style>
</head>
<body>
  <div class="business-card">
    <svg class="card-waves" viewBox="0 0 1000 570" preserveAspectRatio="none" aria-hidden="true">
      <defs>
        <linearGradient id="goldSweep" x1="0" y1="0" x2="1" y2="0">
          <stop offset="0" stop-color="#d4a017"/>
          <stop offset="0.7" stop-color="#c9960f"/>
          <stop offset="1" stop-color="#b8860b"/>
        </linearGradient>
      </defs>
      <path d="M0 332 C 220 290, 420 300, 600 355 C 760 395, 930 330, 1000 180 L1000 570 L0 570 Z" fill="url(#goldSweep)"/>
      <path d="M0 350 C 230 305, 430 320, 610 362 C 790 402, 920 385, 1000 365 L1000 570 L0 570 Z" fill="#c7cad3"/>
      <path d="M0 358 C 230 313, 430 328, 610 370 C 790 410, 920 392, 1000 372 L1000 570 L0 570 Z" fill="#060b18"/>
    </svg>

    <div class="brand">
      <span class="brand-mark"></span>
      <p class="brand-name">Crimson Vantage<br>Cleaning Solutions</p>
    </div>

    <div class="person">
      <p class="person-name">Mara Ellison</p>
      <p class="person-role">Founder</p>
    </div>

    <ul class="contact-list">
      <li>
        <svg viewBox="0 0 24 24"><rect x="6" y="3" width="12" height="18" rx="2" fill="none" stroke="#d4a017" stroke-width="2"/><circle cx="12" cy="18" r="1" fill="#d4a017"/></svg>
        (555) 284-1937
      </li>
      <li>
        <svg viewBox="0 0 24 24"><rect x="2" y="5" width="20" height="14" fill="#d4a017"/><path d="M2 5 L12 13 L22 5" fill="none" stroke="#060b18" stroke-width="1.6"/></svg>
        hello@cvcsclean.com
      </li>
      <li>
        <svg viewBox="0 0 24 24"><circle cx="12" cy="12" r="10" fill="#d4a017"/><path d="M2 12 H22 M12 2 C7 7,7 17,12 22 M12 2 C17 7,17 17,12 22" fill="none" stroke="#060b18" stroke-width="1.2"/></svg>
        www.cvcsclean.com
      </li>
    </ul>

    <p class="address">PO BOX 418 Harbour Lane<br>7 Kestrel Road, Ashford</p>
  </div>
</body>
</html>
```